Business Card Design

Mortgage brokering company, also providing Commercial Finance, Car Finance and Insurance.

Target Market(s)

Home Buyers

Industry/Entity Type

Business

Contact Information for Business Card

All information required on business card is contained in the attachment. Design does not have to follow the style of the attachment.

```html
<!DOCTYPE html>
<html lang="en">
<head>
<meta charset="utf-8">
<title>Corvel Lending – Business Card</title>
<link href="https://fonts.googleapis.com/css2?family=Arimo:wght@400;700&display=swap" rel="stylesheet">
<style>
  :root {
    --backdrop: #3b3b3b;
    --card: #1c1c1c;
    --card-edge: #262626;
    --orange: #f08a1c;
    --orange-light: #f7b267;
    --grey: #8e8e8e;
    --white: #f2f2f2;
  }
  * { box-sizing: border-box; margin: 0; padding: 0; }
  html, body {
    width: 1200px; height: 807px; overflow: hidden;
    background: var(--backdrop);
    font-family: "Arimo", Arial, sans-serif;
  }
  .stage {
    position: relative; width: 1200px; height: 807px;
    display: flex; align-items: center; justify-content: center; gap: 50px;
  }
  .card {
    position: relative; width: 520px; height: 297px;
    background: var(--card);
    border: 1px solid var(--card-edge);
    box-shadow: 0 10px 30px rgba(0,0,0,.45);
    overflow: hidden;
  }

  /* Front */
  .front .accent-disc {
    position: absolute; left: -70px; top: -90px;
    width: 300px; height: 300px; border-radius: 50%;
    background: #232323;
  }
  .front .brand {
    position: absolute; left: 150px; top: 68px;
    font-size: 42px; font-weight: 400; line-height: 1.05;
    color: var(--grey); letter-spacing: 1px;
  }
  .front .services {
    position: absolute; left: 150px; top: 186px;
    font-size: 15px; color: var(--white);
    font-variant: small-caps; letter-spacing: 1px;
    white-space: nowrap;
  }

  /* Back */
  .back .brand-block {
    position: absolute; left: 28px; top: 60px;
    display: flex; align-items: center; gap: 14px;
  }
  .back .brand {
    font-size: 22px; font-weight: 400; color: var(--white); line-height: 1.1;
    text-align: right; width: 120px;
  }
  .back .divider { width: 1px; height: 90px; background: var(--white); }
  .back .brand-disc {
    width: 90px; height: 90px; border-radius: 50%;
    background: radial-gradient(circle at 40% 35%, var(--orange-light), var(--orange) 70%);
  }
  .back .services {
    position: absolute; left: 28px; top: 178px;
    font-size: 14px; color: var(--white);
    font-variant: small-caps; letter-spacing: 1px;
    white-space: nowrap;
  }
  .back .person {
    position: absolute; left: 318px; top: 42px;
  }
  .person .name {
    font-size: 18px; font-weight: 700; color: var(--white);
    font-variant: small-caps; letter-spacing: 1px;
  }
  .person .role { font-size: 12px; color: var(--orange); margin-top: 2px; }
  .contact-list { list-style: none; margin-top: 14px; }
  .contact-list li {
    display: flex; align-items: center; gap: 7px;
    font-size: 11px; color: var(--white); margin-bottom: 6px;
    white-space: nowrap;
  }
  .contact-list svg { width: 12px; height: 12px; fill: none; stroke: var(--orange); stroke-width: 1.6; flex: none; }
  .back .address {
    position: absolute; left: 318px; top: 210px;
    font-size: 11px; color: var(--white); line-height: 1.8;
    font-style: normal;
  }
</style>
</head>
<body>
<main class="stage">
  <section class="card front">
    <div class="accent-disc"></div>
    <h1 class="brand">Corvel<br>Lending</h1>
    <p class="services">Residential | Commercial | Car | Asset</p>
  </section>

  <section class="card back">
    <div class="brand-block">
      <h2 class="brand">Corvel<br>Lending</h2>
      <span class="divider"></span>
      <span class="brand-disc"></span>
    </div>
    <p class="services">Residential | Commercial | Car | Asset</p>

    <div class="person">
      <p class="name">Martin Hale</p>
      <p class="role">Credit Representative</p>
      <ul class="contact-list">
        <li><svg viewBox="0 0 12 12"><path d="M2 1.5h2.5l1 2.5-1.5 1a6 6 0 0 0 3 3l1-1.5 2.5 1V10.5A1 1 0 0 1 9.5 11.5 8.5 8.5 0 0 1 1 3 1 1 0 0 1 2 1.5z"/></svg>07 5550 1234</li>
        <li><svg viewBox="0 0 12 12"><rect x="3" y="1" width="6" height="10" rx="1"/><path d="M5.5 9.3h1"/></svg>0400 555 218</li>
        <li><svg viewBox="0 0 12 12"><rect x="1" y="5" width="10" height="5" rx="1"/><path d="M3 5V1.5h6V5M3 8h6"/></svg>07 5550 1235</li>
        <li><svg viewBox="0 0 12 12"><rect x="1" y="2.5" width="10" height="7"/><path d="M1 2.5l5 4 5-4"/></svg>martin.hale@corvellending.com.au</li>
        <li><svg viewBox="0 0 12 12"><circle cx="6" cy="6" r="5"/><path d="M1 6h10M6 1c2 2.5 2 7.5 0 10M6 1c-2 2.5-2 7.5 0 10"/></svg>www.corvellending.com.au</li>
      </ul>
    </div>
    <address class="address">14 Harbour View Road,<br>Coastal Heights, Qld 4000</address>
  </section>
</main>
</body>
</html>
```